Bluefinch Painting needs a Website

We need a website built for a Painting company I own, we mainly do residential painting, but don't want to be limited to that.

Need to have estimate request form.
Need pic's of past projects

I like the look of the website for http://www.harborline-painters.example
& "Thistledown Property inspections"

My logo that was designed here on ArtHive on the front page

I would like one of the houses I downloaded as part of the background
of the front page.

Target Market(s)

Home owners

Industry/Entity Type

Painting

Number of Pages Required

1 page

Font styles to use
Serif

Requirements
Must have
• Estimate request form for home owners to fill out -
• Name:
• Phone Number:
• Address:
• E-mail:
• Painting project description:
• And my info to:
• My phone number: (555) 318-7764
• My web address bluefinchpainting.example
Nice to have
• My logo that was designed here on ArtHive

```html
<!DOCTYPE html>
<html lang="en">
<head>
<meta charset="utf-8">
<title>Bluefinch Painting</title>
<link rel="stylesheet" href="https://fonts.googleapis.com/css2?family=Open+Sans:wght@400;600;700&display=swap">
<style>
:root{
  --blue:#3d8fd0;
  --blue-dark:#2a6fae;
  --blue-bar:#5aa7e0;
  --blue-band:#4a9ad4;
  --navy:#1c3550;
  --footer:#1f5f8e;
  --services-bg:#5ea6dc;
  --projects-bg:#a9cfea;
  --clients-bg:#eaf3fa;
  --about-bg:#f5f7f9;
  --testimonial:#4f74a8;
  --gauge-red:#e0534f;
  --gauge-blue:#5b8fd0;
  --text:#5b6570;
  --white:#ffffff;
  --field:#e6e8ea;
}
*{margin:0;padding:0;box-sizing:border-box}
html,body{width:1200px;height:2680px;overflow:hidden}
body{position:relative;font-family:"Open Sans",Arial,sans-serif;color:var(--text);background:var(--white)}
.abs{position:absolute}

/* header */
.site-header{left:0;top:0;width:1200px;height:128px;background:var(--white);border-bottom:6px solid var(--blue-band)}
.brand{left:223px;top:22px;display:flex;align-items:center;gap:12px}
.brand-mark{width:46px;height:46px;background:var(--blue)}
.brand-name{font-size:30px;font-weight:700;color:var(--navy);letter-spacing:2px;text-transform:uppercase}
.social{left:1002px;top:28px;display:flex;gap:16px}
.social span{width:26px;height:26px;border-radius:50%;background:var(--blue)}
.main-nav{left:536px;top:82px;display:flex;gap:4px}
.main-nav a{display:block;height:40px;padding:0 14px;line-height:44px;background:var(--blue);color:var(--white);font-size:13px;text-decoration:none;text-transform:uppercase;border-radius:3px 3px 0 0}
.main-nav a.active{background:var(--blue-dark);box-shadow:inset 0 0 0 2px #9ccbef}

/* hero */
.hero{left:0;top:128px;width:1200px;height:334px;background:linear-gradient(180deg,#b8d3ea 0%,#cfd9e0 35%,#8e959a 60%,#5f6a58 85%,#4d5a3f 100%)}
.welcome{left:402px;top:205px;width:387px;height:57px;background:var(--blue);color:var(--white);font-size:32px;text-align:center;line-height:57px;letter-spacing:1px}
.welcome-text{left:402px;top:262px;width:387px;height:72px;background:rgba(30,40,50,.45);color:var(--white);font-size:15px;line-height:22px;text-align:center;padding:12px 20px}
.band{left:0;top:462px;width:1200px;height:14px;background:var(--blue-band)}

/* section head */
.sec-head{left:223px;width:760px;height:38px;background:linear-gradient(90deg,var(--blue-bar),var(--blue));color:var(--navy);font-size:22px;font-weight:600;line-height:38px;padding-left:58px}
.sec-head::before{content:"";position:absolute;left:-14px;top:12px;width:60px;height:14px;background:var(--navy);border-radius:7px}
.copy{left:223px;width:760px;font-size:13px;line-height:19px}

/* about */
.about{left:0;top:476px;width:1200px;height:294px;background:var(--about-bg)}
.why{left:275px;top:636px;font-size:17px;color:#7a8590}
.perks{left:268px;top:680px;list-style:none;font-size:17px;line-height:24px;color:#4a5560}
.perks li{display:flex;align-items:center;gap:10px}
.perks li::before{content:"";width:14px;height:14px;background:var(--blue);border-radius:3px;transform:rotate(45deg)}
.gauge{top:625px}
.gauge-num{font-size:30px;color:#3a4550;text-align:center;width:200px}
.gauge-label{font-size:30px;color:#3a4550;text-align:center;width:200px}

/* clients */
.clients{left:0;top:770px;width:1200px;height:168px;background:var(--clients-bg)}
.clients-title{left:275px;top:780px;font-size:16px;color:#6a7580}
.quote-card{top:818px;width:179px;height:66px;background:var(--testimonial);color:var(--white);font-size:10px;line-height:14px;padding:10px 12px;border-radius:2px}
.quote-card::after{content:"";position:absolute;left:22px;bottom:-10px;border:10px solid transparent;border-bottom:0;border-top-color:var(--testimonial)}
.quote-name{top:896px;font-size:11px;color:#6a7580}

/* services */
.services{left:0;top:938px;width:1200px;height:372px;background:var(--services-bg)}
.service-card{top:1072px;width:179px;height:213px;background:var(--white);text-align:center;padding:16px 14px;box-shadow:0 2px 4px rgba(0,0,0,.15)}
.service-card h3{font-size:14px;font-weight:400;color:#3a4550;margin:16px 0 12px}
.service-card p{font-size:10px;line-height:14px;color:#7a8590;margin-bottom:8px}

/* projects */
.projects{left:0;top:1310px;width:1200px;height:372px;background:var(--projects-bg)}
.project-photo{top:1440px;width:179px;height:130px}
.project-note{top:1570px;width:179px;height:76px;background:var(--white);font-size:10px;line-height:14px;color:#7a8590;padding:12px;text-align:center}

/* quote + contact */
.backdrop{left:0;top:1682px;width:1200px;height:670px;background:linear-gradient(180deg,#c9d6df 0%,#b7c3c8 40%,#9da7a6 70%,#8c9893 100%)}
.veil{left:0;top:1682px;width:1200px;height:670px;background:rgba(255,255,255,.55)}
.label{font-size:15px;color:#2f3a44}
.field{background:var(--field);border:1px solid #d0d4d8}
.btn{background:var(--blue);color:var(--white);font-size:15px;text-align:center;line-height:32px;height:32px;text-transform:uppercase}
.contact-line{display:flex;align-items:center;gap:10px;font-size:15px;color:#2f3a44}
.contact-line.link{color:var(--blue-dark)}

/* map + footer */
.map{left:0;top:2352px;width:1200px;height:268px;background:linear-gradient(120deg,#cfe0c4 0%,#e8e2cf 40%,#a9c8e6 70%,#9cc0e3 100%)}
.site-footer{left:0;top:2620px;width:1200px;height:60px;background:var(--footer);color:var(--white);font-size:14px;text-align:center;line-height:60px}
</style>
</head>
<body>

<header class="site-header abs">
  <div class="brand abs"><span class="brand-mark"></span><span class="brand-name">Bluefinch Painting</span></div>
  <div class="social abs"><span></span><span></span><span></span></div>
  <nav class="main-nav abs">
    <a class="active" href="#home">Home</a>
    <a href="#about">About</a>
    <a href="#services">Services</a>
    <a href="#projects">Projects</a>
    <a href="#quote">Quote Form</a>
    <a href="#contact">Contacts</a>
  </nav>
</header>

<section id="home">
  <div class="hero abs" role="img" aria-label="Photo of a two-storey family house with grey siding and a green front garden"></div>
  <h1 class="welcome abs">WELCOME</h1>
  <p class="welcome-text abs">Vestibulum at fermentum nibh. Maecenas eget massa ac metus porta aliquam. Maecenas quis, aliquet mauris.</p>
  <div class="band abs"></div>
</section>

<section id="about">
  <div class="about abs"></div>
  <h2 class="sec-head abs" style="top:486px">ABOUT US</h2>
  <p class="copy abs" style="top:528px">Vivamus hendrerit convallis lorem, sit amet dui enim a placerat sit amet. Ut rhoncus tellus ac tortor finibus nunc. Vestibulum ornare eros eget lectus rhoncus mattis. Fusce sit amet tincidunt purus. Duis feugiat mauris lacinia, vehicula metus ac egestas orci. In faucibus augue vitae leo convallis, ut semper metus semper. Integer tristique lacus sed sem, luctus placerat velit sit amet lacus. Integer varius viverra urna id rutrum. Duis nec vulputate augue, quis sollicitudin dui. Mauris vel elit ultrices sed sollicitudin sit amet ullamcorper eget magna.</p>
  <p class="why abs">Why Choose Us ?</p>
  <ul class="perks abs">
    <li>Quisque at massa ipsum</li>
    <li>Maecenas a lorem augue</li>
    <li>Cras vitae felis at lacus</li>
  </ul>

  <svg class="gauge abs" style="left:560px" width="200" height="100" viewBox="0 0 200 100" role="img" aria-label="Gauge showing 50 percent">
    <path d="M12 100 A88 88 0 0 1 100 12" fill="none" stroke="var(--gauge-blue)" stroke-width="22"/>
    <path d="M100 12 A88 88 0 0 1 188 100" fill="none" stroke="var(--gauge-red)" stroke-width="22"/>
  </svg>
  <div class="gauge-num abs" style="left:560px;top:672px">50</div>
  <div class="gauge-label abs" style="left:560px;top:728px">Fusce</div>

  <svg class="gauge abs" style="left:765px" width="200" height="100" viewBox="0 0 200 100" role="img" aria-label="Gauge showing 70 percent">
    <path d="M12 100 A88 88 0 0 1 128.4 16.7" fill="none" stroke="var(--gauge-red)" stroke-width="22"/>
    <path d="M128.4 16.7 A88 88 0 0 1 188 100" fill="none" stroke="var(--gauge-blue)" stroke-width="22"/>
  </svg>
  <div class="gauge-num abs" style="left:765px;top:672px">70</div>
  <div class="gauge-label abs" style="left:765px;top:728px">Adipiscing</div>
</section>

<section class="testimonials">
  <div class="clients abs"></div>
  <p class="clients-title abs">What Client's Say ?</p>
  <blockquote class="quote-card abs" style="left:223px">Donec mollis at turpis sed pulvinar. Suspendisse id nibh at eleifend ullamcorper ut sed massa.</blockquote>
  <blockquote class="quote-card abs" style="left:417px">Donec mollis at turpis sed pulvinar. Suspendisse id nibh at eleifend ullamcorper ut sed massa.</blockquote>
  <blockquote class="quote-card abs" style="left:610px">Donec mollis at turpis sed pulvinar. Suspendisse id nibh at eleifend ullamcorper ut sed massa.</blockquote>
  <blockquote class="quote-card abs" style="left:804px">Donec mollis at turpis sed pulvinar. Suspendisse id nibh at eleifend ullamcorper ut sed massa.</blockquote>
  <p class="quote-name abs" style="left:245px">Jenny Doe</p>
  <p class="quote-name abs" style="left:439px">Jenny Doe</p>
  <p class="quote-name abs" style="left:632px">Jenny Doe</p>
  <p class="quote-name abs" style="left:826px">Jenny Doe</p>
</section>

<section id="services">
  <div class="services abs"></div>
  <h2 class="sec-head abs" style="top:948px">Services</h2>
  <p class="copy abs" style="top:1004px;color:var(--white)">Vivamus aliquam sodales pulvinar. Pellentesque eu ligula non massa ullamcorper rutrum ac sit amet quam. Sed ac dolor eros. Aliquam malesuada vestibulum lectus quis accumsan. Aenean sodales mi vitae sem elementum interdum. Curabitur scelerisque neque sit amet luctus congue.</p>

  <article class="service-card abs" style="left:223px">
    <svg width="40" height="40" viewBox="0 0 40 40" aria-hidden="true"><rect x="4" y="6" width="26" height="10" rx="2" fill="#333"/><path d="M30 11h5v10H20v6" fill="none" stroke="#333" stroke-width="3"/><rect x="17" y="27" width="6" height="11" rx="1" fill="#333"/></svg>
    <h3>Exterior Painting</h3>
    <p>Donec mollis at turpis sed pulvinar. Suspendisse id nibh at eleifend ullamcorper.</p>
    <p>Aliquam pellentesque tellus nunc vitae, posuere lacus dapibus.</p>
  </article>
  <article class="service-card abs" style="left:417px">
    <svg width="40" height="40" viewBox="0 0 40 40" aria-hidden="true"><rect x="4" y="6" width="26" height="10" rx="2" fill="#333"/><path d="M30 11h5v10H20v6" fill="none" stroke="#333" stroke-width="3"/><rect x="17" y="27" width="6" height="11" rx="1" fill="#333"/></svg>
    <h3>Interior Painting</h3>
    <p>Donec mollis at turpis sed pulvinar. Suspendisse id nibh at eleifend ullamcorper.</p>
    <p>Aliquam pellentesque tellus nunc vitae, posuere lacus dapibus.</p>
  </article>
  <article class="service-card abs" style="left:610px">
    <svg width="40" height="40" viewBox="0 0 40 40" aria-hidden="true"><rect x="4" y="6" width="26" height="10" rx="2" fill="#333"/><path d="M30 11h5v10H20v6" fill="none" stroke="#333" stroke-width="3"/><rect x="17" y="27" width="6" height="11" rx="1" fill="#333"/></svg>
    <h3>Residential Painting</h3>
    <p>Donec mollis at turpis sed pulvinar. Suspendisse id nibh at eleifend ullamcorper.</p>
    <p>Aliquam pellentesque tellus nunc vitae, posuere lacus dapibus.</p>
  </article>
  <article class="service-card abs" style="left:804px">
    <svg width="40" height="40" viewBox="0 0 40 40" aria-hidden="true"><rect x="4" y="6" width="26" height="10" rx="2" fill="#333"/><path d="M30 11h5v10H20v6" fill="none" stroke="#333" stroke-width="3"/><rect x="17" y="27" width="6" height="11" rx="1" fill="#333"/></svg>
    <h3>Commercial Painting</h3>
    <p>Donec mollis at turpis sed pulvinar. Suspendisse id nibh at eleifend ullamcorper.</p>
    <p>Aliquam pellentesque tellus nunc vitae, posuere lacus dapibus.</p>
  </article>
</section>

<section id="projects">
  <div class="projects abs"></div>
  <h2 class="sec-head abs" style="top:1318px">Projects</h2>
  <p class="copy abs" style="top:1372px;color:#3a4a5a">Suspendisse lobortis accumsan dui sit amet faucibus. Integer viverra ultrices ex id posuere. Integer laoreet, nunc imperdiet eleifend, erat quam mollis nunc, non tincidunt felis nulla nec magna. Vestibulum consequat mollis diam sed sollicitudin. Integer elementum commodo ligula pulvinar bibendum.</p>

  <div class="project-photo abs" style="left:223px;background:linear-gradient(180deg,#c8d6e2,#8a8f8c 55%,#5d6b4e)" role="img" aria-label="Photo of a large painted two-storey home"></div>
  <div class="project-photo abs" style="left:417px;background:linear-gradient(180deg,#9fc3e6,#b59a74 55%,#5f7a45)" role="img" aria-label="Photo of a beige painted house with a lawn"></div>
  <div class="project-photo abs" style="left:610px;background:linear-gradient(180deg,#a8c8e8,#8d8a86 55%,#4f6b3e)" role="img" aria-label="Photo of a freshly painted suburban house with flowers"></div>
  <div class="project-photo abs" style="left:804px;background:linear-gradient(180deg,#b8d4ec,#c6c0b4 55%,#6c7d58)" role="img" aria-label="Photo of a white house with a driveway"></div>

  <p class="project-note abs" style="left:223px">Aliquam pellentesque tellus nunc vitae. Sed tincidunt nulla ex, quis ultrices lorem dapibus a.</p>
  <p class="project-note abs" style="left:417px">Aliquam pellentesque tellus nunc vitae. Sed tincidunt nulla ex, quis ultrices lorem dapibus a.</p>
  <p class="project-note abs" style="left:610px">Aliquam pellentesque tellus nunc vitae. Sed tincidunt nulla ex, quis ultrices lorem dapibus a.</p>
  <p class="project-note abs" style="left:804px">Aliquam pellentesque tellus nunc vitae. Sed tincidunt nulla ex, quis ultrices lorem dapibus a.</p>
</section>

<div class="backdrop abs" role="img" aria-label="Faded photo of a company work van parked in front of a house"></div>
<div class="veil abs"></div>

<section id="quote">
  <h2 class="sec-head abs" style="top:1690px">Free Quote</h2>
  <p class="copy abs" style="top:1740px;color:#2f3a44">Convallis ac sem sit amet, mattis tempor urna. In efficitur malesuada lacinia. Vestibulum imperdiet suscipit aliquam. Suspendisse condimentum varius lectus, eu placerat elit posuere vitae.</p>
  <span class="label abs" style="left:268px;top:1792px">Name</span>
  <div class="field abs" style="left:342px;top:1790px;width:298px;height:28px"></div>
  <span class="label abs" style="left:268px;top:1834px">Phone Nr</span>
  <div class="field abs" style="left:342px;top:1832px;width:298px;height:28px"></div>
  <span class="label abs" style="left:268px;top:1876px">Address</span>
  <div class="field abs" style="left:342px;top:1874px;width:298px;height:28px"></div>
  <span class="label abs" style="left:268px;top:1918px">E-mail</span>
  <div class="field abs" style="left:342px;top:1916px;width:298px;height:28px"></div>
  <span class="label abs" style="left:655px;top:1796px">Painting project description</span>
  <div class="field abs" style="left:655px;top:1830px;width:322px;height:118px"></div>
  <div class="btn abs" style="left:855px;top:1955px;width:128px">Send</div>
</section>

<section id="contact">
  <h2 class="sec-head abs" style="top:2015px">Contact</h2>
  <p class="copy abs" style="top:2066px;color:#2f3a44">Convallis ac sem sit amet, mattis tempor urna. In efficitur malesuada lacinia. Vestibulum imperdiet suscipit aliquam. Suspendisse condimentum varius lectus, eu placerat elit posuere vitae.</p>
  <span class="label abs" style="left:268px;top:2124px">Name</span>
  <div class="field abs" style="left:342px;top:2122px;width:298px;height:28px"></div>
  <span class="label abs" style="left:268px;top:2166px">E-mail</span>
  <div class="field abs" style="left:342px;top:2164px;width:298px;height:28px"></div>
  <div class="field abs" style="left:342px;top:2200px;width:298px;height:80px"></div>
  <div class="btn abs" style="left:521px;top:2298px;width:128px">Send</div>

  <span class="label abs" style="left:705px;top:2122px;text-transform:uppercase">Address</span>
  <div class="contact-line abs" style="left:705px;top:2160px">
    <svg width="18" height="24" viewBox="0 0 18 24" aria-hidden="true"><path d="M9 0a9 9 0 0 0-9 9c0 7 9 15 9 15s9-8 9-15a9 9 0 0 0-9-9z" fill="var(--blue)"/><circle cx="9" cy="9" r="3.5" fill="#fff"/></svg>
    <span>123 Interdum tristique est con<br>modo pharetra</span>
  </div>
  <div class="contact-line abs" style="left:705px;top:2220px">
    <svg width="18" height="18" viewBox="0 0 18 18" aria-hidden="true"><path d="M4 1l3 4-2 2c1 2 3 4 5 5l2-2 4 3-2 4C7 17 1 11 0 4z" fill="#3a4550"/></svg>
    <span>(555) 318-7764</span>
  </div>
  <div class="contact-line link abs" style="left:705px;top:2252px">
    <svg width="18" height="14" viewBox="0 0 18 14" aria-hidden="true"><rect x="1" y="1" width="16" height="12" fill="none" stroke="var(--blue)" stroke-width="2"/><path d="M1 1l8 7 8-7" fill="none" stroke="var(--blue)" stroke-width="2"/></svg>
    <span>info@bluefinchpainting.example</span>
  </div>
</section>

<div class="map abs" role="img" aria-label="Street map of the local service area"></div>

<footer class="site-footer abs">© 2015 Bluefinch Painting. All Rights Reserved.</footer>

</body>
</html>
```